vireo nuts company small package

we are looking to design a package for our nuts 10cm by 13 cm and also 3.25 inch by 4.5 inches. our nuts are:
Salted peanuts
honey roasted peanuts
salted cashews
honey roasted cashews
pistachios
sunflower seeds

have a floral design simple yet elegant not too crowded
our product is non GMO

some of our competitors:
http://kestrabite.example/
http://www.dovuhusk.example/sg/
http://tirotiro.example/en/content/view/5/17/

Target Market(s)

european market, Middle eastern market

Industry/Entity Type

It Company

Font styles to use
Decorative
Script

Requirements
Must have
• floral design not crowded yet elegant
• high resolution pictures of the nuts
Nice to have
Should not have
• cartoon characters

```html
<!DOCTYPE html>
<html lang="en">
<head>
<meta charset="utf-8">
<title>Vireo – snack pouches</title>
<link href="https://fonts.googleapis.com/css2?family=Oswald:wght@500&family=Courgette&display=swap" rel="stylesheet">
<style>
  :root{
    --page:#ffffff;
    --seeds-bag:#a9aaac;
    --seeds-bag-light:#c4c5c7;
    --seeds-dark:#3b3b3c;
    --seeds-accent:#f2e24a;
    --pist-bag:#c9da2b;
    --pist-bag-light:#dbe84a;
    --pist-dark:#4b6a2b;
    --pist-accent:#3da3db;
    --type-light:#ffffff;
  }
  *{margin:0;padding:0;box-sizing:border-box}
  html,body{width:1200px;height:848px;overflow:hidden;background:var(--page)}
  .canvas{position:relative;width:1200px;height:848px}
  .pouch{position:absolute;top:172px;width:417px;height:572px}
  .pouch--seeds{left:100px;--bag:var(--seeds-bag);--bag-light:var(--seeds-bag-light);--dark:var(--seeds-dark);--accent:var(--seeds-accent)}
  .pouch--pistachio{left:640px;--bag:var(--pist-bag);--bag-light:var(--pist-bag-light);--dark:var(--pist-dark);--accent:var(--pist-accent)}
  .pouch__art{position:absolute;inset:0;width:100%;height:100%}
  .brand{position:absolute;left:0;width:430px;top:102px;text-align:center;
    font-family:'Oswald',sans-serif;font-weight:500;font-size:64px;line-height:1;letter-spacing:1px;color:var(--type-light)}
  .tagline{position:absolute;font-family:'Courgette',cursive;color:var(--accent);line-height:1}
  .tagline--premium{left:276px;top:404px;font-size:19px}
  .tagline--percent{left:295px;top:498px;font-size:17px}
  .tagline--natural{left:300px;top:516px;font-size:14px}
  .product-name{position:absolute;left:192px;font-family:'Oswald',sans-serif;font-weight:500;
    color:var(--type-light);font-size:36px;line-height:1;letter-spacing:.5px}
  .pouch--pistachio .product-name{left:195px}
  .pouch--pistachio .tagline--premium{left:255px}
  .pouch--pistachio .tagline--percent{left:297px;top:476px}
  .pouch--pistachio .tagline--natural{left:292px;top:496px}
</style>
</head>
<body>
<main class="canvas">

  <section class="pouch pouch--seeds">
    <svg class="pouch__art" viewBox="0 0 417 572">
      <defs>
        <linearGradient id="bagSeeds" x1="0" x2="1"><stop offset="0" stop-color="var(--seeds-bag)"/><stop offset=".5" stop-color="var(--seeds-bag-light)"/><stop offset="1" stop-color="var(--seeds-bag)"/></linearGradient>
        <linearGradient id="seedsPhoto" x1="0" y1="0" x2="1" y2="1"><stop offset="0" stop-color="#2c2c2e"/><stop offset=".5" stop-color="#6d6e70"/><stop offset="1" stop-color="#1f1f20"/></linearGradient>
      </defs>
      <rect class="bag" x="0" y="0" width="417" height="572" fill="url(#bagSeeds)"/>
      <g class="seal" fill="var(--seeds-bag-light)"><rect y="4" width="417" height="4"/><rect y="14" width="417" height="4"/><rect y="24" width="417" height="4"/></g>
      <rect class="logo-frame" role="img" aria-label="ornamental floral frame around the brand name" x="70" y="55" width="290" height="160" rx="40" fill="var(--seeds-dark)"/>
      <path class="window" role="img" aria-label="photo of black striped sunflower seeds" d="M78 462 C50 350 150 252 300 252 C350 252 388 258 410 240 C392 322 322 362 240 392 C170 418 112 440 78 462 Z" fill="url(#seedsPhoto)"/>
      <path class="swoosh" d="M45 500 C110 440 210 420 290 390 C370 355 404 300 415 232 C398 330 330 372 250 400 C170 428 100 450 45 500 Z" fill="var(--seeds-dark)"/>
      <g class="seed-icons" role="img" aria-label="two small sunflower seed illustrations" fill="var(--seeds-dark)">
        <ellipse cx="176" cy="456" rx="7" ry="11" transform="rotate(40 176 456)"/>
        <ellipse cx="160" cy="494" rx="10" ry="16" transform="rotate(35 160 494)"/>
      </g>
    </svg>
    <div class="brand">VIREO</div>
    <div class="tagline tagline--premium">Premium</div>
    <div class="product-name" style="top:430px">SUNFLOWER</div>
    <div class="product-name" style="top:476px">SEEDS</div>
    <div class="tagline tagline--percent">100%</div>
    <div class="tagline tagline--natural">natural</div>
  </section>

  <section class="pouch pouch--pistachio">
    <svg class="pouch__art" viewBox="0 0 417 572">
      <defs>
        <linearGradient id="bagPist" x1="0" x2="1"><stop offset="0" stop-color="var(--pist-bag)"/><stop offset=".5" stop-color="var(--pist-bag-light)"/><stop offset="1" stop-color="var(--pist-bag)"/></linearGradient>
        <linearGradient id="pistPhoto" x1="0" y1="0" x2="1" y2="1"><stop offset="0" stop-color="#a8794d"/><stop offset=".5" stop-color="#e2c49a"/><stop offset="1" stop-color="#8f6238"/></linearGradient>
      </defs>
      <rect class="bag" x="0" y="0" width="417" height="572" fill="url(#bagPist)"/>
      <g class="seal" fill="var(--pist-bag-light)"><rect y="4" width="417" height="4"/><rect y="14" width="417" height="4"/><rect y="24" width="417" height="4"/></g>
      <rect class="logo-frame" role="img" aria-label="ornamental floral frame around the brand name" x="70" y="55" width="290" height="160" rx="40" fill="var(--pist-dark)"/>
      <path class="window" role="img" aria-label="photo of roasted pistachios in shell" d="M78 462 C50 350 150 252 300 252 C350 252 388 258 410 240 C392 322 322 362 240 392 C170 418 112 440 78 462 Z" fill="url(#pistPhoto)"/>
      <path class="swoosh" d="M45 500 C110 440 210 420 290 390 C370 355 404 300 415 232 C398 330 330 372 250 400 C170 428 100 450 45 500 Z" fill="var(--pist-dark)"/>
      <g class="nut-icons" role="img" aria-label="two small pistachio illustrations" fill="#d9c39a">
        <ellipse cx="170" cy="470" rx="12" ry="10"/>
        <ellipse cx="222" cy="490" rx="20" ry="15"/>
      </g>
    </svg>
    <div class="brand">VIREO</div>
    <div class="tagline tagline--premium">Premium</div>
    <div class="product-name" style="top:430px">PISTACHIOS</div>
    <div class="tagline tagline--percent">100%</div>
    <div class="tagline tagline--natural">natural</div>
  </section>

</main>
</body>
</html>
```